Business cards for 3 Realtors at one brokerage

We will need a business card template that can be projected on 3 business cards. Harborline Homes & Capital Corp. has 3 realtors on staff Dale, Owen, and Marcus. We all want a business card that shows our new logo and information. I will attach many versions of our Logo as well as head shots for each realtor (Owen- Long hair, youngest. Marcus- Suit jacket, parted hair cut. Dale- Angled Pose, Shirt and Tie.) I have attached our information below.

Dale Pinsworth
801-555-0147
dale@harborlinehomesco.com
Principal Broker

Marcus Ferndale
801-555-0192
marcus@harborlinehomesco.com
Real Estate Agent

Owen Ferndale
801-555-0163
owen@harborlinehomesco.com
Real Estate Agent

Harborline Homes & Capital Corp.
HarborlineHomesCo.com
2918 E 8250 Suite 207-316, Millbrook Falls, UT 84120

Please feel free to reach out with any questions, comments, or concerns.

```html
<!DOCTYPE html>
<html lang="en">
<head>
<meta charset="utf-8">
<title>Harborline Homes &amp; Capital Corp. — Business Cards</title>
<link rel="stylesheet" href="https://fonts.googleapis.com/css2?family=Montserrat:wght@400;500;700&display=swap">
<style>
  :root {
    --backdrop: #bdbdbd;
    --card: #1c1d1f;
    --card-edge: #2f86c9;
    --accent: #36a3ec;
    --silver: #b9bcc0;
    --text: #e9eaec;
    --muted: #8a8d91;
    --photo-light: #8e9196;
    --photo-dark: #3a3c40;
  }
  * { box-sizing: border-box; margin: 0; padding: 0; }
  html, body { width: 1200px; height: 800px; overflow: hidden; }
  body {
    background: var(--backdrop);
    font-family: "Montserrat", sans-serif;
    display: flex;
    align-items: center;
    justify-content: center;
    gap: 40px;
  }
  .card {
    position: relative;
    width: 560px;
    height: 320px;
    background: var(--card);
    border-radius: 24px;
    box-shadow: 0 4px 0 var(--card-edge), 0 14px 30px rgba(0,0,0,.25);
    overflow: hidden;
  }

  /* Brand mark (name + plain circle) */
  .brand { display: flex; align-items: center; gap: 14px; }
  .brand-circle {
    width: 54px; height: 54px; border-radius: 50%;
    border: 4px solid currentColor; flex: none;
  }
  .brand-name {
    font-weight: 700; font-size: 15px; line-height: 1.35;
    letter-spacing: .12em; text-transform: uppercase;
  }

  /* Back: contact side */
  .card-back .brand {
    position: absolute; left: 34px; top: 128px; width: 230px;
    color: var(--accent);
  }
  .card-back .brand-name { color: var(--silver); }
  .card-back .brand-circle { color: var(--accent); }
  .divider {
    position: absolute; left: 280px; top: 40px; bottom: 40px;
    width: 1px;
    background: linear-gradient(to bottom, transparent, #55585d 50%, transparent);
  }
  .contact {
    position: absolute; left: 306px; top: 62px; right: 20px;
    color: var(--text);
  }
  .agent-name {
    color: var(--accent); font-weight: 700; font-size: 19px;
    letter-spacing: .03em; text-transform: uppercase;
  }
  .agent-title { color: var(--muted); font-size: 12px; margin: 2px 0 12px; }
  .address { font-size: 11.5px; line-height: 1.55; margin-bottom: 14px; }
  .contact-list { list-style: none; font-size: 11.5px; line-height: 1.9; }
  .contact-list li { display: flex; align-items: center; gap: 9px; white-space: nowrap; }
  .contact-list svg { width: 12px; height: 12px; fill: var(--accent); flex: none; }

  /* Front: photo side */
  .card-front .brand {
    position: absolute; left: 48px; top: 120px; width: 280px;
    color: var(--silver);
  }
  .headshot {
    position: absolute; right: 0; top: 0; bottom: 0; width: 220px;
    background: radial-gradient(ellipse at 50% 35%, var(--photo-light), var(--photo-dark) 75%);
  }
</style>
</head>
<body>

  <section class="card card-back">
    <div class="brand">
      <span class="brand-circle"></span>
      <span class="brand-name">Harborline Homes &amp; Capital Corp.</span>
    </div>
    <div class="divider"></div>
    <div class="contact">
      <h1 class="agent-name">Marcus Ferndale</h1>
      <p class="agent-title">Real Estate Agent</p>
      <p class="address">Harborline Homes &amp; Capital Corp.<br>2918 E 8250 Suite 207-316<br>Millbrook Falls, UT 84120</p>
      <ul class="contact-list">
        <li><svg viewBox="0 0 24 24"><path d="M6.6 10.8a15.1 15.1 0 0 0 6.6 6.6l2.2-2.2c.3-.3.7-.4 1-.2 1.1.4 2.3.6 3.6.6.6 0 1 .4 1 1V20c0 .6-.4 1-1 1C10.6 21 3 13.4 3 4c0-.6.4-1 1-1h3.5c.6 0 1 .4 1 1 0 1.3.2 2.5.6 3.6.1.3 0 .7-.2 1z"/></svg>801-555-0192</li>
        <li><svg viewBox="0 0 24 24"><path d="M2 5h20v14H2zm2 2v.5l8 5 8-5V7zm0 3v7h16v-7l-8 5z"/></svg>marcus@harborlinehomesco.com</li>
        <li><svg viewBox="0 0 24 24"><path d="M12 2a10 10 0 1 0 0 20 10 10 0 0 0 0-20zm0 2c1 0 2.3 2 2.8 5H9.2C9.7 6 11 4 12 4zm-7.7 7h3.8a17 17 0 0 0 0 2H4.3a8 8 0 0 1 0-2zm5.8 0h3.8a15 15 0 0 1 0 2h-3.8a15 15 0 0 1 0-2zm5.8 0h3.8a8 8 0 0 1 0 2h-3.8a17 17 0 0 0 0-2zM9.2 15h5.6c-.5 3-1.8 5-2.8 5s-2.3-2-2.8-5z"/></svg>HarborlineHomesCo.com</li>
      </ul>
    </div>
  </section>

  <section class="card card-front">
    <div class="brand">
      <span class="brand-circle"></span>
      <span class="brand-name">Harborline Homes &amp; Capital Corp.</span>
    </div>
    <div class="headshot" role="img" aria-label="Headshot of Marcus Ferndale in a grey plaid suit jacket and light blue shirt"></div>
  </section>

</body>
</html>
```